Digital billboard sales for the nema region

Business card that is informative and unique. Whether the card can be applicable to a real world application or it is 3D or if something changed on the card. I want it to be an eye catcher

Went on vacation/holiday

```html
<!DOCTYPE html>
<html lang="en">
<head>
<meta charset="utf-8">
<title>Business Card – Front and Back</title>
<link rel="stylesheet" href="https://fonts.googleapis.com/css2?family=Roboto:wght@300;400;500;700&display=swap">
<style>
  :root {
    --backdrop: #c3d0da;
    --card-paper: #e6e6ea;
    --navy: #364d63;
    --steel: #6f8fa6;
    --ink: #111114;
    --paper-text: #e9edf1;
  }
  * { margin: 0; padding: 0; box-sizing: border-box; }
  html, body {
    width: 1200px;
    height: 840px;
    overflow: hidden;
  }
  body {
    background: var(--backdrop);
    display: flex;
    flex-direction: column;
    align-items: center;
    justify-content: center;
    gap: 36px;
    font-family: "Roboto", Arial, sans-serif;
  }
  .card {
    width: 560px;
    height: 362px;
    display: block;
    box-shadow: 0 10px 24px rgba(40, 60, 80, 0.25);
  }
  .brand-light { font-weight: 300; fill: var(--ink); }
  .brand-bold { font-weight: 500; fill: var(--ink); }
  .slogan { font-weight: 700; fill: var(--ink); }
  .person-name { font-weight: 300; fill: var(--paper-text); }
  .person-name-bold { font-weight: 700; }
  .person-role { font-weight: 500; fill: var(--paper-text); letter-spacing: 4px; }
  .contact-text { font-weight: 700; fill: var(--ink); letter-spacing: 0.6px; }
  .icon { fill: var(--ink); }
</style>
</head>
<body>

  <svg class="card card-front" viewBox="0 0 675 437" aria-label="Business card front">
    <defs>
      <linearGradient id="paper" x1="0" y1="0" x2="1" y2="0">
        <stop offset="0" stop-color="#e8e8ee"/>
        <stop offset="0.6" stop-color="#dedde2"/>
        <stop offset="1" stop-color="#cacacf"/>
      </linearGradient>
    </defs>
    <rect class="paper" width="675" height="437" fill="url(#paper)"/>
    <polygon class="band-top" points="0,0 575,0 605,40 0,40" fill="var(--navy)"/>
    <polygon class="corner-top" points="602,0 675,0 675,30 626,30" fill="var(--steel)"/>
    <polygon class="band-bottom" points="140,398 675,398 675,437 101,437" fill="var(--navy)"/>
    <polygon class="corner-bottom" points="0,411 97,411 67,437 0,437" fill="var(--steel)"/>
    <text x="181" y="219" font-size="47" textLength="369" lengthAdjust="spacingAndGlyphs"><tspan class="brand-light">BUSINESS </tspan><tspan class="brand-bold">NAME</tspan></text>
    <text class="slogan" x="194" y="247" font-size="14" textLength="335" lengthAdjust="spacing">SLOGAN FOR COMPANY HERE</text>
  </svg>

  <svg class="card card-back" viewBox="0 0 675 437" aria-label="Business card back">
    <rect class="paper" width="675" height="437" fill="url(#paper)"/>
    <polygon class="band-top" points="0,0 590,0 560,30 0,30" fill="var(--navy)"/>
    <polygon class="name-panel" points="0,78 360,78 400,118 360,158 0,158" fill="var(--navy)"/>
    <text class="person-name" x="30" y="122" font-size="34">DARA <tspan class="person-name-bold">WHITLOW</tspan></text>
    <text class="person-role" x="32" y="142" font-size="11">ART DIRECTOR</text>

    <g class="contact-list">
      <g class="contact-email">
        <rect class="icon" x="330" y="205" width="20" height="14"/>
        <polyline points="330,205 340,213 350,205" fill="none" stroke="#e6e6ea" stroke-width="1.6"/>
        <text class="contact-text" x="362" y="217" font-size="12">INFO@BRIGHTLANE.COM</text>
      </g>
      <g class="contact-phone">
        <path class="icon" d="M334 240c0 10 7 18 16 19l2-5-5-2-2 2c-3-2-5-4-6-7l2-2-2-5z"/>
        <text class="contact-text" x="362" y="247" font-size="12">+44 7305 1186</text>
        <text class="contact-text" x="362" y="262" font-size="12">+44 7305 2291</text>
      </g>
      <g class="contact-address">
        <path class="icon" d="M340 280a8 8 0 0 1 8 8c0 6-8 14-8 14s-8-8-8-14a8 8 0 0 1 8-8zm0 5a3 3 0 1 0 0 6 3 3 0 0 0 0-6z"/>
        <text class="contact-text" x="362" y="295" font-size="12">14 HARBOUR ROAD, DUBAI</text>
      </g>
    </g>

    <polygon class="band-bottom" points="0,398 535,398 574,437 0,437" fill="var(--navy)"/>
    <polygon class="corner-bottom" points="578,411 675,411 675,437 608,437" fill="var(--steel)"/>
  </svg>

</body>
</html>
```